Single Splash Web Page as Long Term Placeholder

I registered the url PebbleAndPine.com. This is the name of a business I will be starting several years down the road. It will be a coffee (drips) and ice cream (dips) store located in a beach town somewhere on the east coast of the US, probably in the Outer Banks of NC. I need a single page that will have the name of the business and the text:

Coming eventually to a beach near you!

The page should somehow reflect the beach environment.

```html
<!DOCTYPE html>
<html lang="en">
<head>
<meta charset="utf-8">
<title>Pebble &amp; Pine — Coming eventually to a beach near you</title>
<link rel="stylesheet" href="https://fonts.googleapis.com/css2?family=Oswald:wght@500;600&display=swap">
<style>
  :root {
    --sky-top: #d3e3ec;
    --sky-haze: #cfe1ea;
    --sky-blue: #2f7fc4;
    --sky-soft: #7fb2d6;
    --horizon-haze: #9cc3da;
    --horizon: #b7d3e2;
    --sea-deep: #154f86;
    --sea-mid: #2a7fb2;
    --sea-shallow: #4fa3bf;
    --foam: #eef5f5;
    --wash: #c9e0de;
    --sand-light: #ece2cf;
    --sand: #ddcfb4;
    --accent-teal: #1ea5b0;
    --text-light: #ffffff;
    --text-shade: rgba(10, 50, 90, 0.55);
  }
  html, body {
    margin: 0;
    padding: 0;
    width: 1200px;
    height: 1000px;
    overflow: hidden;
  }
  .splash {
    position: relative;
    width: 1200px;
    height: 1000px;
    overflow: hidden;
    font-family: "Oswald", "Arial Narrow", sans-serif;
  }
  .beach-backdrop {
    position: absolute;
    inset: 0;
    background: linear-gradient(
      to bottom,
      var(--sky-top) 0%,
      var(--sky-haze) 14%,
      var(--sky-blue) 24%,
      var(--sky-blue) 38%,
      var(--sky-soft) 48%,
      var(--horizon-haze) 56%,
      var(--horizon) 62.7%,
      var(--sea-deep) 62.9%,
      var(--sea-mid) 69%,
      var(--sea-shallow) 72%,
      var(--foam) 75%,
      var(--foam) 78%,
      var(--wash) 82%,
      var(--sand-light) 85%,
      var(--sand) 100%
    );
  }
  .brand {
    position: absolute;
    left: 0;
    right: 0;
    top: 432px;
    display: flex;
    justify-content: center;
    align-items: center;
    gap: 14px;
  }
  .brand-dot {
    width: 40px;
    height: 40px;
    border-radius: 50%;
    background: var(--accent-teal);
  }
  .brand-name {
    margin: 0;
    font-size: 46px;
    font-weight: 600;
    letter-spacing: 1px;
    line-height: 1;
    text-transform: uppercase;
    color: var(--text-light);
  }
  .tagline {
    position: absolute;
    left: 0;
    right: 0;
    top: 594px;
    margin: 0;
    text-align: center;
    font-size: 26px;
    font-weight: 500;
    line-height: 1.2;
    text-transform: uppercase;
    color: var(--text-light);
    text-shadow: 0 1px 3px var(--text-shade);
  }
</style>
</head>
<body>
  <main class="splash">
    <div class="beach-backdrop" role="img" aria-label="Photograph of a sunny beach: blue sky with white clouds, deep blue ocean with breaking waves and pale sand in the foreground"></div>
    <div class="brand">
      <span class="brand-dot"></span>
      <h1 class="brand-name">Pebble &amp; Pine</h1>
    </div>
    <p class="tagline">Coming eventually to a beach near you!</p>
  </main>
</body>
</html>
```